LumaWear e-commerce website design for storefrontly platform

I currently have a trendy e-commerce clothing store that is primarily based off of the Southern California Style/Trends. I am looking for a redesign of my storefrontly template as I don't like my current image. I am looking for a sleek clean design that allows more focus on the products. I like neutral backgrounds and easy to use websites. Should be responsive to mobile devices. I would also like to have some ideas for a slide show picture that notifies customers of free shipping if possible. I do also have a theme template that I purchased through Storefrontly so one could set the theme up for me and edit it to what I need. My website is lumawear-example.com if you would like to look at the type of products I have. I am also looking to do a logo redesign as well- looking for a more stylish logo that would appeal to an approximate age range of 18-40 year old women. I want to be remembered, something to match the web design.

I like teal/turquoise and grey combos but I don't have to have this as the colors.

Target Market(s)

approx. 18-40

Industry/Entity Type

E-Commerce

Number of Pages Required

2 page

Requirements
Must have
• Menu bar, storefrontly compatible, easy to access/navigate, responsive to mobile devices, easy product upload
Nice to have
• if able ability to resize pictures all to the same size
Should not have
• not be difficult to navigate both on a reg. computer or mobile device

```html
<!DOCTYPE html>
<html lang="en">
<head>
<meta charset="utf-8">
<title>LumaWear – Home</title>
<link rel="stylesheet" href="https://fonts.googleapis.com/css2?family=Arimo:wght@400;700&display=swap">
<style>
:root{
  --coral:#f47c72;
  --coral-dark:#e8685e;
  --ink:#222222;
  --text:#3a3a3a;
  --muted:#8a8a8a;
  --header-bg:#e9e9e9;
  --paper:#f0f0f0;
  --white:#ffffff;
  --dark-btn:#2e2e2e;
  --footer-bg:#ebebeb;
  --card-bg:#f3f3f3;
}
*{box-sizing:border-box;margin:0;padding:0}
html,body{width:1200px;height:2932px;overflow:hidden}
body{position:relative;font-family:"Arimo",Arial,sans-serif;color:var(--text);background:var(--white)}

/* top bar */
.topbar{position:absolute;left:0;top:0;width:1200px;height:47px;background:var(--coral);color:var(--white);font-size:17px}
.topbar .mail{position:absolute;left:121px;top:13px;display:flex;align-items:center;gap:12px}
.topbar .login{position:absolute;left:706px;top:13px;display:flex;align-items:center;gap:10px}
.topbar .social{position:absolute;left:885px;top:8px;display:flex;gap:4px}
.topbar .social span{width:29px;height:29px;background:var(--coral-dark);border:1px solid rgba(255,255,255,.5);display:block}

/* header */
.header{position:absolute;left:0;top:47px;width:1200px;height:191px;background:var(--header-bg)}
.brand{position:absolute;left:121px;top:30px;display:flex;align-items:center;gap:12px;font-weight:700;font-size:48px;color:var(--ink)}
.brand i{width:22px;height:22px;border-radius:50%;background:var(--coral);display:block}
.cart{position:absolute;left:674px;top:57px;width:196px;height:37px;background:#dcdcdc;border:1px solid #cfcfcf;display:flex;align-items:center;gap:12px;padding-left:18px;font-size:15px;color:#333}
.cart em{font-style:normal;color:var(--coral)}
.search{position:absolute;left:879px;top:57px;width:201px;height:37px;background:#dcdcdc;border:1px solid #cfcfcf;display:flex;align-items:center;justify-content:space-between;padding:0 14px;font-size:15px;color:#333}
.nav{position:absolute;left:98px;top:125px;height:66px;display:flex;background:#f4f4f4;border:1px solid #d8d8d8}
.nav a{display:flex;align-items:center;justify-content:center;height:64px;font-size:22px;color:var(--ink);text-decoration:none;border-right:1px solid #d6d6d6}
.nav a.active{background:var(--coral);color:var(--white)}

/* hero */
.hero{position:absolute;left:0;top:238px;width:1200px;height:460px;background:linear-gradient(100deg,#d9a15a 0%,#c9833e 25%,#efe2d0 48%,#e6c7a6 62%,#c47a3a 85%,#a65f2c 100%)}

/* about */
.about{position:absolute;left:0;top:698px;width:1200px;height:517px;background:var(--paper)}
.about .hero-shadow{position:absolute;left:14px;top:0;width:1172px;height:38px;background:linear-gradient(#b8b8b8,rgba(200,200,200,0));clip-path:polygon(0 0,100% 0,98% 100%,2% 100%)}
.about .model{position:absolute;left:166px;top:2px;width:150px;height:492px;background:linear-gradient(#d9b3a8,#c0506a 30%,#2a2222 55%,#2a2222 70%,#e2c0a6 90%,#8a5a3a)}
.section-title{display:flex;align-items:center;gap:14px;color:var(--ink)}
.section-title .rule{height:2px;background:#555}
.section-title .dot{width:13px;height:13px;border-radius:50%;background:var(--ink)}
.about .section-title{position:absolute;left:316px;top:40px;font-size:31px}
.about p{position:absolute;left:316px;top:100px;width:690px;font-size:20px;line-height:29px;color:var(--ink)}
.btn-dark{position:absolute;background:var(--dark-btn);color:var(--white);border-radius:4px;display:flex;align-items:center;justify-content:center}
.about .btn-dark{left:906px;top:427px;width:139px;height:35px;font-size:20px}

/* what's new */
.new{position:absolute;left:0;top:1215px;width:1200px;height:637px;background:var(--white)}
.new .section-title{position:absolute;left:121px;top:35px;font-size:28px}
.pager{position:absolute;left:1037px;display:flex;gap:4px}
.pager span{width:19px;height:20px;background:var(--coral);display:flex;align-items:center;justify-content:center}
.product{position:absolute;top:114px;width:260px;height:453px;background:var(--card-bg);box-shadow:0 2px 10px rgba(0,0,0,.18)}
.product .photo{position:absolute;left:0;top:0;width:260px;height:186px}
.product .price{position:absolute;right:6px;top:4px;width:60px;height:60px;border-radius:50%;background:var(--coral);color:var(--white);font-size:14px;display:flex;align-items:center;justify-content:center;transform:rotate(45deg)}
.product h3{position:absolute;left:0;top:200px;width:260px;text-align:center;font-size:16px;font-weight:400;color:var(--coral)}
.product p{position:absolute;left:22px;top:236px;width:216px;text-align:center;font-size:14px;line-height:20px;color:#555}
.product .bar{position:absolute;left:0;bottom:0;width:260px;height:31px;background:var(--coral);display:flex;align-items:center;padding-left:12px;color:var(--white)}
.product .stars{font-size:15px;letter-spacing:1px;color:#ffd43a}
.product .stars b{color:var(--white);font-weight:400}
.product .go{margin-left:26px;font-size:16px;font-weight:700;letter-spacing:1px;color:#3a2a2a}
.product .carticon{position:absolute;right:4px;top:3px;width:25px;height:25px;background:var(--ink);display:flex;align-items:center;justify-content:center}

/* seasonal */
.seasonal{position:absolute;left:0;top:1852px;width:1200px;height:766px;background:var(--paper)}
.seasonal .section-title{position:absolute;left:121px;top:52px;font-size:28px}
.pick{position:absolute;width:430px;height:258px;background:var(--white);box-shadow:0 2px 10px rgba(0,0,0,.15)}
.pick .photo{position:absolute;left:4px;top:7px;width:186px;height:244px;border:3px solid #111}
.pick h3{position:absolute;left:210px;top:14px;width:210px;font-size:22px;font-weight:400;line-height:26px;color:var(--coral)}
.pick p{position:absolute;left:210px;width:200px;font-size:16px;line-height:20px;color:#888}
.pick .btn-dark{left:294px;top:214px;width:117px;height:33px;font-size:16px}

/* footer */
.footer{position:absolute;left:0;top:2618px;width:1200px;height:248px;background:var(--footer-bg);font-size:14px;line-height:25px;color:#555}
.footer h4{position:absolute;font-size:17px;font-weight:700;color:var(--coral)}
.footer .map{position:absolute;left:121px;top:78px;width:141px;height:118px;background:linear-gradient(135deg,#e3e1d9,#cfd7c6 60%,#e6e3da)}
.footer .addr{position:absolute;left:281px;top:70px;width:260px}
.footer .links{position:absolute;left:588px;top:68px;line-height:20px}
.footer .divider{position:absolute;left:791px;top:22px;width:1px;height:200px;background:#cfcfcf}
.footer .news{position:absolute;left:813px;top:54px;width:270px;font-size:14px;line-height:20px;color:#777}
.footer .email{position:absolute;left:813px;top:131px;width:266px;height:35px;background:var(--coral);color:var(--white);font-size:15px;display:flex;align-items:center;padding-left:10px}
.footer .submit{position:absolute;left:813px;top:188px;width:77px;height:25px;background:var(--ink);color:var(--white);font-size:13px;font-weight:700;display:flex;align-items:center;justify-content:center}

.bottombar{position:absolute;left:0;top:2866px;width:1200px;height:66px;background:var(--coral);color:var(--white);font-size:14px}
.bottombar .legal{position:absolute;left:123px;top:24px}
.bottombar .copy{position:absolute;left:442px;top:24px}
.bottombar .social{position:absolute;left:895px;top:18px;display:flex;gap:12px}
.bottombar .social span{width:29px;height:29px;background:var(--coral-dark);border:1px solid rgba(255,255,255,.45);display:block}
</style>
</head>
<body>

<div class="topbar">
  <div class="mail">
    <svg width="22" height="16" viewBox="0 0 22 16"><rect x="1" y="1" width="20" height="14" fill="none" stroke="#fff" stroke-width="2"/><path d="M1 1l10 8 10-8" fill="none" stroke="#fff" stroke-width="2"/></svg>
    <span>Email us at: info@lumawear-example.com</span>
  </div>
  <div class="login">
    <svg width="20" height="20" viewBox="0 0 20 20"><circle cx="10" cy="10" r="9" fill="#fff"/><circle cx="10" cy="8" r="3" fill="#f47c72"/><path d="M4 16c2-4 10-4 12 0" fill="#f47c72"/></svg>
    <span>Login/Register</span>
  </div>
  <div class="social"><span></span><span></span><span></span><span></span><span></span><span></span></div>
</div>

<header class="header">
  <div class="brand"><span>LumaWear</span><i></i></div>
  <div class="cart">
    <svg width="20" height="18" viewBox="0 0 20 18"><path d="M1 2h3l2 10h10l2-7H5" fill="none" stroke="#444" stroke-width="2"/><circle cx="8" cy="15.5" r="1.6" fill="#444"/><circle cx="15" cy="15.5" r="1.6" fill="#444"/></svg>
    <span>My Cart (<em>0 items</em>)</span>
  </div>
  <div class="search">
    <span>Search Item..</span>
    <svg width="18" height="18" viewBox="0 0 18 18"><circle cx="7" cy="7" r="5.5" fill="none" stroke="#222" stroke-width="2.4"/><path d="M11 11l5.5 5.5" stroke="#222" stroke-width="2.6"/></svg>
  </div>
  <nav class="nav">
    <a class="active" style="width:166px">Whats New?</a>
    <a style="width:117px">Dresses</a>
    <a style="width:73px">Tops</a>
    <a style="width:211px">Bottoms/Rompers</a>
    <a style="width:219px">Shoes/Accessories</a>
    <a style="width:74px">Sale</a>
    <a style="width:142px;border-right:none">About Me</a>
  </nav>
</header>

<div class="hero" role="img" aria-label="Photo of two smiling women carrying shopping bags"></div>

<section class="about">
  <div class="hero-shadow"></div>
  <div class="model" role="img" aria-label="Photo of a model in a floral top and black skirt"></div>
  <div class="section-title">
    <span class="rule" style="width:140px"></span><span class="dot"></span>
    <span>About Our Visit</span>
    <span class="dot"></span><span class="rule" style="width:260px"></span>
  </div>
  <p>Lorem Ipsum is simply dummy text of the printing and typesetting industry. Lorem Ipsum has been the industry's standard dummy text ever since the 1500s, when an unknown printer took a galley of type and scrambled it to make a type specimen book. It has survived not only five centuries, but also the leap into electronic typesetting, remaining essentially unchanged. It was popularised in the 1960s with the release of Lettersheet sheets containing Lorem Ipsum passages, and more recently with desktop publishing software like Pageform Studio including versions of Lorem Ipsum.</p>
  <div class="btn-dark">Read More</div>
</section>

<section class="new">
  <div class="section-title"><span>Wats New ?</span><span class="dot" style="width:11px;height:11px"></span><span class="rule" style="width:260px;height:1px"></span></div>
  <div class="pager" style="top:47px">
    <span><svg width="8" height="10" viewBox="0 0 8 10"><path d="M6 1L2 5l4 4" fill="none" stroke="#fff" stroke-width="2"/></svg></span>
    <span><svg width="8" height="10" viewBox="0 0 8 10"><path d="M2 1l4 4-4 4" fill="none" stroke="#fff" stroke-width="2"/></svg></span>
  </div>

  <article class="product" style="left:166px">
    <div class="photo" role="img" aria-label="Product photo of a brown cutout ankle boot" style="background:linear-gradient(#ffffff 20%,#6b5646 45%,#3e2f26 70%,#ffffff 90%)"></div>
    <div class="price">$50.00</div>
    <h3>Sienna Cutout Boot</h3>
    <p>Totally amazing booties with side cutouts and metal buckle accents. Slip in with heel buckle closure. Super comfy leather (man made). Heel height 2.5 inches</p>
    <div class="bar"><span class="stars">★★★★<b>★</b></span><span class="go">Click Here</span>
      <span class="carticon"><svg width="16" height="14" viewBox="0 0 20 18"><path d="M1 2h3l2 10h10l2-7H5" fill="none" stroke="#fff" stroke-width="2.2"/><circle cx="8" cy="15.5" r="1.8" fill="#fff"/><circle cx="15" cy="15.5" r="1.8" fill="#fff"/></svg></span></div>
  </article>

  <article class="product" style="left:469px">
    <div class="photo" role="img" aria-label="Product photo of a long white and navy kimono cardigan" style="background:linear-gradient(90deg,#ffffff 20%,#d8d4d6 40%,#2a2a36 50%,#d8d4d6 60%,#ffffff 80%)"></div>
    <div class="price">$47.00</div>
    <h3>Coralie Kimono Cardigan-Navy</h3>
    <p>Amazing maxi kimono cardigan featuring a navy dip dye at the bottom. Totally cool with some skinnies and a simple draped white tee. Match with booties and statement jewelry for a perfect outfit. Material-100% Rayon (doesn't have too much stretch)...</p>
    <div class="bar"><span class="stars">★★★★<b>★</b></span><span class="go">Click Here</span>
      <span class="carticon"><svg width="16" height="14" viewBox="0 0 20 18"><path d="M1 2h3l2 10h10l2-7H5" fill="none" stroke="#fff" stroke-width="2.2"/><circle cx="8" cy="15.5" r="1.8" fill="#fff"/><circle cx="15" cy="15.5" r="1.8" fill="#fff"/></svg></span></div>
  </article>

  <article class="product" style="left:773px">
    <div class="photo" role="img" aria-label="Product photo of a model in a patterned blue playsuit" style="background:linear-gradient(#d9a070 0%,#b06a4a 25%,#2e4a8a 50%,#7a3a5a 70%,#2a3e78 100%)"></div>
    <div class="price">$42.00</div>
    <h3>Marisol Playsuit</h3>
    <p>Talk about an amazing playsuit for this fall season ahead! This romper features long bell sleeves that flare from the elbow, a front overlay, and cinched elastic waist. Paired with a pair of strappy flats or ankle booties and bold...</p>
    <div class="bar"><span class="stars">★★★★<b>★</b></span><span class="go">Click Here</span>
      <span class="carticon"><svg width="16" height="14" viewBox="0 0 20 18"><path d="M1 2h3l2 10h10l2-7H5" fill="none" stroke="#fff" stroke-width="2.2"/><circle cx="8" cy="15.5" r="1.8" fill="#fff"/><circle cx="15" cy="15.5" r="1.8" fill="#fff"/></svg></span></div>
  </article>
</section>

<section class="seasonal">
  <div class="section-title"><span>Seasonal Must Haves</span><span class="dot" style="width:11px;height:11px"></span><span class="rule" style="width:260px;height:1px"></span></div>
  <div class="pager" style="top:62px">
    <span><svg width="8" height="10" viewBox="0 0 8 10"><path d="M6 1L2 5l4 4" fill="none" stroke="#fff" stroke-width="2"/></svg></span>
    <span><svg width="8" height="10" viewBox="0 0 8 10"><path d="M2 1l4 4-4 4" fill="none" stroke="#fff" stroke-width="2"/></svg></span>
  </div>

  <article class="pick" style="left:150px;top:116px">
    <div class="photo" role="img" aria-label="Photo of a model in a patterned blue playsuit" style="background:linear-gradient(#e8d2c0,#2e4a8a 40%,#7a3a5a 65%,#2a3e78)"></div>
    <h3>Marisol Playsuit</h3>
    <p style="top:50px">Lorem Ipsum is simply dummy text of the printing and typesetting industry. Lorem Ipsum has been the industry's standard dummy text ever since the 1500s, when an unknown printer</p>
    <div class="btn-dark">View Details</div>
  </article>

  <article class="pick" style="left:627px;top:116px">
    <div class="photo" role="img" aria-label="Photo of a model in a white bell sleeve fringe tube top" style="background:linear-gradient(#f4f4f4,#e8d8c4 35%,#ffffff 60%,#d8cfc6)"></div>
    <h3>Nola Bell Sleeve Fringe Tube Top</h3>
    <p style="top:76px">Lorem Ipsum is simply dummy text of the printing and typesetting industry. Lorem Ipsum has been the industry's standard dummy text ever since the 1500s.</p>
    <div class="btn-dark">View Details</div>
  </article>

  <article class="pick" style="left:150px;top:438px">
    <div class="photo" role="img" aria-label="Photo of white lace bell bottom trousers" style="background:linear-gradient(#c9b7a6,#ece6dc 40%,#f6f2ea 70%,#cdbfb0)"></div>
    <h3>Juniper Bell Bottoms</h3>
    <p style="top:50px">Lorem Ipsum is simply dummy text of the printing and typesetting industry. Lorem Ipsum has been the industry's standard dummy text ever since the 1500s, when an unknown printer</p>
    <div class="btn-dark">View Details</div>
  </article>

  <article class="pick" style="left:627px;top:438px">
    <div class="photo" role="img" aria-label="Photo of patterned blue sheer bell bottom trousers" style="background:linear-gradient(90deg,#eef0f2,#3a5a80 30%,#6a8aa8 50%,#3a5a80 70%,#eef0f2)"></div>
    <h3>Harlow Sheer Bells</h3>
    <p style="top:50px">Lorem Ipsum is simply dummy text of the printing and typesetting industry. Lorem Ipsum has been the industry's standard dummy text ever since the 1500s, when an unknown printer</p>
    <div class="btn-dark">View Details</div>
  </article>
</section>

<footer class="footer">
  <h4 style="left:123px;top:40px">Address</h4>
  <div class="map" role="img" aria-label="Small street map showing the store location"></div>
  <div class="addr">Lorem Ipsum is simply dummy text of the printing and typesetting industry<br>Phone: (555) 430-0172<br>Email: lumawear@info.com</div>
  <h4 style="left:588px;top:40px">Important Links</h4>
  <div class="links">Whats New?<br>Dresses<br>Tops<br>Bottoms/Rompers<br>Shoes/Accessories<br>Sale<br>About Me</div>
  <div class="divider"></div>
  <h4 style="left:813px;top:30px;font-size:15px;letter-spacing:.5px">NEWS LETTER</h4>
  <div class="news">Lorem Ipsum is simply dummy text of the printing and typesetting industry. Lorem Ipsum has been the</div>
  <div class="email">Your Email</div>
  <div class="submit">SUBMIT</div>
</footer>

<div class="bottombar">
  <div class="legal">Site Map &nbsp;|&nbsp; Privacy &nbsp;|&nbsp; Site Credits</div>
  <div class="copy">All Rights Reserved@ 2014 lumawear@info.com</div>
  <div class="social"><span></span><span></span><span></span><span></span><span></span></div>
</div>

</body>
</html>
```